Online Course Page

We are building a video based online course page. This project is for only the actual page that the student will watch the videos at. They will watch one vide at a time. Once one video lesson is completed then they can move to the next video lesson. The page will need to show the video player. (Main feature.) The list of lessons in the course. Instructor information. Profile picture and bio of the instructor. A Live chat button that will initiate a chat in real-time with the instructor.

The winning designer will also be asked to to design the dashboard area and other aspects of the user interface as an additional project.

Target Market(s)

Adults

Number of Pages Required

1 page

Colors
9bcb3c

Requirements
Must have
• Our logo is attached. Green and grey are our colors. Should feel modern, clean and be simple to navigate. The site will be responsive so the layout should work well on mobile devices.

```html
<!DOCTYPE html>
<html lang="en">
<head>
<meta charset="utf-8">
<title>LearnGrove – Online Course</title>
<link href="https://fonts.googleapis.com/css2?family=Catamaran:wght@500;600;700&family=Lato:wght@400;700&display=swap" rel="stylesheet">
<style>
:root{
  --green:#8cc63f;
  --green-dark:#7ab52f;
  --ink:#1d1d1d;
  --text:#444;
  --muted:#777;
  --header-bg:#f6f6f7;
  --section-bg:#f0f0f2;
  --card-border:#e2e2e4;
  --footer-bg:#333333;
  --white:#ffffff;
}
*{box-sizing:border-box;margin:0;padding:0}
html,body{width:762px;height:1200px;overflow:hidden;background:var(--white)}
body{position:relative;font-family:"Lato",sans-serif;color:var(--text)}
.abs{position:absolute}
.heading{font-family:"Catamaran",sans-serif;color:var(--ink)}

/* header */
.site-header{left:0;top:0;width:762px;height:70px;background:var(--header-bg)}
.brand{left:90px;top:22px;display:flex;align-items:center;gap:6px;font-family:"Catamaran",sans-serif;font-weight:700;font-size:20px;color:var(--green)}
.brand-dot{width:14px;height:14px;border-radius:50%;background:var(--green)}
.contact{left:421px;top:27px;display:flex;align-items:center;gap:7px;font-size:9px;font-weight:700;color:var(--ink)}
.live-chat{left:577px;top:25px;width:60px;height:22px;border:1.5px solid var(--ink);border-radius:11px;font-family:"Catamaran",sans-serif;font-weight:600;font-size:11px;color:var(--ink);display:flex;align-items:center;justify-content:center}
.menu-btn{left:649px;top:24px;width:24px;height:24px;border:1.5px solid var(--ink);border-radius:50%}

/* hero */
.hero-title{left:0;width:762px;top:76px;text-align:center;font-size:20px;font-weight:700}
.video-player{left:180px;top:114px;width:402px;height:192px;border-radius:7px;background:linear-gradient(100deg,#6b4a2c 0%,#8a9a5a 35%,#b9c58a 55%,#c98a5a 75%,#d8d2c8 100%)}
.play-btn{left:364px;top:193px;width:34px;height:34px;border-radius:50%;background:rgba(255,255,255,.9)}
.arrow{top:192px}
.hero-sub{left:0;width:762px;top:317px;text-align:center;font-size:18px;font-weight:600}
.hero-text{left:115px;width:532px;top:347px;text-align:center;font-size:7px;line-height:11px;color:#333}
.btn{top:384px;height:22px;border-radius:11px;font-size:9px;font-weight:700;display:flex;align-items:center;justify-content:center}
.btn-primary{left:298px;width:81px;background:var(--green);color:var(--white)}
.btn-outline{left:388px;width:76px;border:1px solid #cfcfcf;color:var(--green);background:var(--white)}

/* courses */
.courses{left:0;top:435px;width:762px;height:417px;background:var(--section-bg)}
.section-title{left:0;width:762px;text-align:center;font-size:23px;font-weight:700;display:flex;justify-content:center;align-items:center;gap:8px}
.title-dot{width:16px;height:16px;border-radius:50%;background:var(--green)}
.course-card{top:597px;width:170px;height:201px;background:var(--white);border:2px solid var(--card-border);border-radius:6px}
.course-thumb{top:-42px;left:43px;width:80px;height:80px;border-radius:50%;border:3px solid var(--green);background:linear-gradient(135deg,#dfe6ea,#9fb0b8)}
.course-title{top:52px;left:0;width:166px;text-align:center;font-size:10.5px;line-height:14px;color:var(--ink);font-weight:500;font-family:"Catamaran",sans-serif}
.course-desc{top:88px;left:14px;width:138px;text-align:center;font-size:7px;line-height:11px}
.author{top:133px;left:34px;display:flex;align-items:center;gap:10px;font-size:7px;font-weight:700;color:var(--ink)}
.author-pic{width:30px;height:30px;border-radius:50%;background:linear-gradient(#b7a79a,#4d5560)}
.card-foot{top:176px;left:0;width:166px;height:23px;border-top:1px solid #ececec;display:flex;align-items:center;justify-content:space-between;padding:0 10px;font-size:8px}
.card-foot .watch{color:var(--green);display:flex;align-items:center;gap:4px}
.stats{display:flex;gap:8px;color:var(--ink)}

/* instructors */
.instructor{top:964px;width:120px;text-align:center}
.instructor-photo{margin:0 auto;width:78px;height:88px;position:relative}
.instructor-photo::before{content:"";position:absolute;left:0;top:10px;width:78px;height:78px;border-radius:50%;background:radial-gradient(circle at 50% 75%,#7d8480 0%,#8f9a7c 28%,var(--green) 58%)}
.photo-shadow{margin:4px auto 0;width:60px;height:4px;border-radius:50%;background:#e6e6e6}
.instructor-name{margin-top:15px;font-size:11px;font-weight:700;font-family:"Catamaran",sans-serif;color:var(--ink)}
.instructor-role{font-size:8px;color:var(--muted);margin-top:1px}
.socials{display:flex;justify-content:center;gap:4px;margin-top:6px}
.socials i{width:13px;height:13px;border-radius:50%;border:1px solid var(--green)}
.socials i.fill{background:var(--green)}

/* footer */
.site-footer{left:0;top:1168px;width:762px;height:32px;background:var(--footer-bg);color:var(--white)}
.copyright{left:90px;top:11px;font-size:8px}
.footer-social{left:586px;top:6px;display:flex;gap:5px}
.footer-social i{width:19px;height:19px;border-radius:50%;border:1.5px solid var(--white)}
</style>
</head>
<body>

<header class="abs site-header">
  <div class="abs brand"><span class="brand-dot"></span>LearnGrove</div>
  <div class="abs contact">
    <svg width="22" height="16" viewBox="0 0 22 16"><rect x="1" y="1" width="20" height="14" rx="1" fill="none" stroke="#8cc63f" stroke-width="1.6"/><path d="M1 1l10 8 10-8" fill="none" stroke="#8cc63f" stroke-width="1.6"/></svg>
    hello@learngrove.com
  </div>
  <div class="abs live-chat">Live Chat</div>
  <div class="abs menu-btn">
    <svg width="21" height="21" viewBox="0 0 21 21"><circle cx="10.5" cy="10.5" r="8" fill="#8cc63f"/><path d="M6.5 7.5h8M6.5 10.5h8M6.5 13.5h8" stroke="#1d1d1d" stroke-width="1.3"/></svg>
  </div>
</header>

<h1 class="abs heading hero-title">We Provide Online Video Based Education Training</h1>
<svg class="abs arrow" style="left:134px" width="12" height="20" viewBox="0 0 12 20"><path d="M10 2L2 10l8 8" fill="none" stroke="#1d1d1d" stroke-width="2.2"/></svg>
<div class="abs video-player" role="img" aria-label="Video still of a smiling student studying outdoors with a laptop and notes"></div>
<div class="abs play-btn"><svg width="34" height="34" viewBox="0 0 34 34"><path d="M14 10l9 7-9 7z" fill="#1d1d1d"/></svg></div>
<svg class="abs arrow" style="left:597px;top:198px" width="12" height="20" viewBox="0 0 12 20"><path d="M2 2l8 8-8 8" fill="none" stroke="#1d1d1d" stroke-width="2.2"/></svg>
<h2 class="abs heading hero-sub">Autem vel eum iriure dolor in hendrerit.</h2>
<p class="abs hero-text">Lorem ipsum dolor sit amet, consectetuer adipiscing elit, sed diam nonummy nibh euismod tincidunt ut laoreet dolore magna aliquam erat volutpat. Ut wisi enim ad minim veniam, quis nostrud exerci tation ullamcorper suscipit lobortis nisl ut aliquip ex ea commodo consequat.</p>
<div class="abs btn btn-primary">Watch Video</div>
<div class="abs btn btn-outline">Next Video</div>

<section class="abs courses"></section>
<h2 class="abs heading section-title" style="top:478px"><span class="title-dot"></span>Top Courses</h2>

<article class="abs course-card" style="left:90px">
  <div class="abs course-thumb" role="img" aria-label="Course photo of a learner at a desk with a computer"></div>
  <h3 class="abs course-title">Lorem Ipsum Dolor Sit Amet,<br>Consectetur Adipiscing</h3>
  <p class="abs course-desc">Lorem ipsum dolor sit amet, consectetuer adipiscing elit, sed diam nonummy nibh euismod tincidunt ut laoreet dolore</p>
  <div class="abs author"><span class="author-pic" role="img" aria-label="Instructor portrait"></span>By: Daniel Reyes</div>
  <div class="abs card-foot"><span class="watch"><svg width="9" height="9" viewBox="0 0 9 9"><circle cx="4.5" cy="4.5" r="4" fill="none" stroke="#8cc63f"/><path d="M3.5 3l2.5 1.5-2.5 1.5z" fill="#8cc63f"/></svg>Watch Video</span><span class="stats"><span>&#9679; 85</span><span>&#9675; 35</span></span></div>
</article>
<article class="abs course-card" style="left:296px">
  <div class="abs course-thumb" role="img" aria-label="Course photo of a student writing in a library"></div>
  <h3 class="abs course-title">Lorem Ipsum Dolor Sit Amet,<br>Consectetur Adipiscing</h3>
  <p class="abs course-desc">Lorem ipsum dolor sit amet, consectetuer adipiscing elit, sed diam nonummy nibh euismod tincidunt ut laoreet dolore</p>
  <div class="abs author"><span class="author-pic" role="img" aria-label="Instructor portrait"></span>By: Daniel Reyes</div>
  <div class="abs card-foot"><span class="watch"><svg width="9" height="9" viewBox="0 0 9 9"><circle cx="4.5" cy="4.5" r="4" fill="none" stroke="#8cc63f"/><path d="M3.5 3l2.5 1.5-2.5 1.5z" fill="#8cc63f"/></svg>Watch Video</span><span class="stats"><span>&#9679; 85</span><span>&#9675; 35</span></span></div>
</article>
<article class="abs course-card" style="left:502px">
  <div class="abs course-thumb" role="img" aria-label="Course photo of a learner with headphones at a laptop"></div>
  <h3 class="abs course-title">Lorem Ipsum Dolor Sit Amet,<br>Consectetur Adipiscing</h3>
  <p class="abs course-desc">Lorem ipsum dolor sit amet, consectetuer adipiscing elit, sed diam nonummy nibh euismod tincidunt ut laoreet dolore</p>
  <div class="abs author"><span class="author-pic" role="img" aria-label="Instructor portrait"></span>By: Daniel Reyes</div>
  <div class="abs card-foot"><span class="watch"><svg width="9" height="9" viewBox="0 0 9 9"><circle cx="4.5" cy="4.5" r="4" fill="none" stroke="#8cc63f"/><path d="M3.5 3l2.5 1.5-2.5 1.5z" fill="#8cc63f"/></svg>Watch Video</span><span class="stats"><span>&#9679; 85</span><span>&#9675; 35</span></span></div>
</article>

<h2 class="abs heading section-title" style="top:895px"><span class="title-dot"></span>About Instructors</h2>

<div class="abs instructor" style="left:113px">
  <div class="instructor-photo" role="img" aria-label="Portrait of instructor Aaron Holt"></div>
  <div class="photo-shadow"></div>
  <div class="instructor-name">Prof. Aaron Holt</div>
  <div class="instructor-role">- Exercitation Ullamnd</div>
  <div class="socials"><i></i><i class="fill"></i><i></i></div>
</div>
<div class="abs instructor" style="left:251px">
  <div class="instructor-photo" role="img" aria-label="Portrait of instructor Marta Quill"></div>
  <div class="photo-shadow"></div>
  <div class="instructor-name">Prof. Marta Quill</div>
  <div class="instructor-role">- Exercitation Ullamnd</div>
  <div class="socials"><i></i><i class="fill"></i><i></i></div>
</div>
<div class="abs instructor" style="left:389px">
  <div class="instructor-photo" role="img" aria-label="Portrait of instructor Owen Pratt"></div>
  <div class="photo-shadow"></div>
  <div class="instructor-name">Prof. Owen Pratt</div>
  <div class="instructor-role">- Exercitation Ullamnd</div>
  <div class="socials"><i></i><i class="fill"></i><i></i></div>
</div>
<div class="abs instructor" style="left:528px">
  <div class="instructor-photo" role="img" aria-label="Portrait of instructor Lena Fairow"></div>
  <div class="photo-shadow"></div>
  <div class="instructor-name">Prof. Lena Fairow</div>
  <div class="instructor-role">- Exercitation Ullamnd</div>
  <div class="socials"><i></i><i class="fill"></i><i></i></div>
</div>

<footer class="abs site-footer">
  <p class="abs copyright">Copyright © 2018 LearnGrove. All Right Reserved.</p>
  <div class="abs footer-social"><i></i><i></i><i></i><i></i></div>
</footer>

</body>
</html>
```